Professional & attention grabbing.

A business card design, front and back. I already have a logo I will attach, but I am open to something new as well.
Things to include:
Name:
Title:
Phone:
Email:
Wanting something that is professional but attention grabbing.
Also we do a lot of work using drones on natural gas pipelines (leading the future)if you want to include any of that. I'm open to ideas.
Target Market(s)
Natural gas transmission industry / greenhouse gas mitigation industry
Industry/Entity Type
Business
Contact Information for Business Card
All details have been conveyed above.
Colors
Designer to choose colors to be used in the design.
Look and feel
Each slider illustrates characteristics of the customer's brand and the style your logo design should communicate.

```html
<!DOCTYPE html>
<html lang="en">
<head>
<meta charset="utf-8">
<title>Corvane Inspections – Business Card</title>
<link rel="stylesheet" href="https://fonts.googleapis.com/css2?family=Open+Sans:wght@400;600&display=swap">
<style>
  :root {
    --page-bg: #e6e4e1;
    --card-bg: #1b1b1b;
    --card-back-bg: #181818;
    --accent-red: #c1272d;
    --text-white: #f2f2f2;
    --mark-grey: #555555;
  }
  * { margin: 0; padding: 0; box-sizing: border-box; }
  html, body { width: 1200px; height: 1000px; overflow: hidden; }
  body {
    position: relative;
    background: var(--page-bg);
    font-family: "Open Sans", Arial, sans-serif;
  }
  .card {
    position: absolute;
    left: 266px;
    width: 666px;
    height: 397px;
  }
  .card--front { top: 74px; background: var(--card-bg); }
  .card--back { top: 533px; background: var(--card-back-bg); }

  .brand {
    position: absolute;
    display: flex;
    align-items: center;
  }
  .brand__square { background: var(--accent-red); flex: none; }
  .brand__name {
    font-weight: 600;
    letter-spacing: 1px;
    line-height: 1;
  }
  .card--front .brand { left: 97px; top: 102px; width: 188px; height: 191px; gap: 12px; }
  .card--front .brand__square { width: 26px; height: 26px; }
  .card--front .brand__name { color: var(--text-white); font-size: 30px; }

  .card--back .brand { left: 129px; top: 122px; gap: 26px; }
  .card--back .brand__square { width: 150px; height: 150px; background: var(--mark-grey); }
  .card--back .brand__name { color: var(--mark-grey); font-size: 42px; line-height: 1.25; }

  .details {
    position: absolute;
    left: 367px;
    top: 99px;
    color: var(--text-white);
    font-size: 16px;
    line-height: 24px;
  }
  .details__name {
    color: var(--accent-red);
    font-size: 21px;
    font-weight: 600;
    letter-spacing: 0.5px;
    line-height: 26px;
  }
  .details__address { margin-top: 18px; }
  .contact-list { list-style: none; margin-top: 10px; }
  .contact-list li { display: flex; align-items: center; gap: 8px; height: 24.5px; }
  .contact-list svg { width: 14px; height: 14px; fill: var(--accent-red); flex: none; }
</style>
</head>
<body>
  <section class="card card--front">
    <div class="brand">
      <span class="brand__square"></span>
      <span class="brand__name">CORVANE</span>
    </div>
    <div class="details">
      <p class="details__name">ELIAS MARROW</p>
      <p class="details__title">Managing Director</p>
      <p class="details__address">4120 North Alder Lane<br>Hagerstown, MD 21740</p>
      <ul class="contact-list">
        <li>
          <svg viewBox="0 0 16 16" aria-hidden="true"><path d="M2 6c0-2 3-3 6-3s6 1 6 3v1h-3V6H5v1H2zM4 8h8l2 5H2z"/></svg>
          + 000 000 0000
        </li>
        <li>
          <svg viewBox="0 0 16 16" aria-hidden="true"><path d="M1 3h14v10H1zM2 4l6 5 6-5z" fill-rule="evenodd"/></svg>
          info@corvane.com
        </li>
        <li>
          <svg viewBox="0 0 16 16" aria-hidden="true"><path d="M8 1a7 7 0 1 0 0 14A7 7 0 0 0 8 1zm0 2a5 5 0 0 1 4.5 2.8H9.5L8 4.5 6 6l1 2-2 1-1.5-2.5A5 5 0 0 1 8 3zm1 7 2.5.5-1 2.8A5 5 0 0 1 8 13z"/></svg>
          www.corvane.com
        </li>
      </ul>
    </div>
  </section>

  <section class="card card--back">
    <div class="brand">
      <span class="brand__square"></span>
      <span class="brand__name">CORVANE<br>INSPECTIONS</span>
    </div>
  </section>
</body>
</html>
```